MES Modul-Struktur grafisch veranschaulichen
Zielgruppe
Wir sind Software-Hersteller. Thema 'MES'. Unsere Kunden sind Produktionsunternehmen.
Mit einem MES (Manufacturing Execution System) werden Produktionsprozesse überwacht, geplant, gesteuert und optimiert. Allgemein geht es darum, die Produktivität zu steigern und Kosten zu minimieren.
Eine MES-Software ist modular strukturiert, so dass der Kunde sich nach Bedarf die einzelnen Funktionsmodule zusammenstellen kann. Unser MES MORVIK 7 MAX besteht z.B. aus folgenden Einzelmodulen:
- BASIS (Basismodul)
- MDE (Maschinendatenerfassung)
- BDE (Betriebsdatenerfassung)
- INST (Instandhaltung)
- ALARM (Alarmierung)
- DOK (Dokumentenmanagement)
- TNT (Traceability)
- PLAN (Feinplanung/Leitstand)
- LOG (Logistik)
- VIS (Visualisierung)
- PEP (Personaleinsatzplanung)
- MPZE (Personalzeiterfassung)
- DNC (Rezepturen/DNC)
- EM (Energiemonitoring)
Aufgabenstellung
Die modulare Struktur und der große Umfang an Modulen ist ein wichtiger Vorteil für unsere Kunden, da Sie nicht so schnell an Grenzen stoßen und sich dann unter Umständen eine weitere Insellösung (extra Software mit extra Datenbank ...) anschaffen müssen.
Wichtig ist, dass die einzelnen Module funktionell ineinandergreifen und alle auf die gleiche Datenbank zugreifen.
Es reicht wenn in der Grafik die Module nur mit er Abkürzung, also z.B. MDE bezeichnet werden. Für den ersten Entwurf können auch Platzhalter genutzt werden.
Der Betrachter sollte aus der Grafik auf den ersten Blick erkennen:
- umfängliches MES
- modular strukturiert
- Funktionsmodule step-by-step erweiterbar
Für die Umsetzung naheliegend wären Puzzle-Steine, Stapolos, ... muss aber nicht.

```html
<!DOCTYPE html>
<html lang="de">
<head>
<meta charset="utf-8">
<title>MES Modulstruktur</title>
<link href="https://fonts.googleapis.com/css2?family=PT+Sans:wght@400;700&display=swap" rel="stylesheet">
<style>
  :root {
    --bg-center: #fbfcfc;
    --bg-edge: #dce1e4;
    --link-edge: #d3d9dc;
    --ring: #ffffff;
    --text: #ffffff;
    --basis: #9fb3c1;
    --bde: #f0a81a;
    --alarm: #d9542a;
    --mde: #a5b92e;
    --inst: #e37d1c;
    --plan: #1d4a32;
    --tnt: #5c9d34;
    --dok: #1f6d42;
    --pep: #6fb2dc;
    --mpze: #2a8a4a;
    --log: #3b3366;
    --vis: #3187c2;
    --dnc: #6a3a6c;
    --em: #255c9c;
  }
  html, body { margin: 0; padding: 0; overflow: hidden; }
  .canvas {
    width: 1200px; height: 1050px; position: relative; overflow: hidden;
    background: radial-gradient(ellipse at 50% 50%, var(--bg-center) 35%, var(--bg-edge) 100%);
  }
  .module-map { position: absolute; inset: 0; }
  .link-edge { stroke: var(--link-edge); stroke-width: 14; }
  .link-core { stroke: var(--ring); stroke-width: 10; }
  .ring { fill: var(--ring); }
  .code { font-family: "PT Sans", sans-serif; font-weight: 700; font-size: 29px; fill: var(--text); text-anchor: middle; }
  .name { font-family: "PT Sans", sans-serif; font-weight: 400; font-size: 13px; fill: var(--text); text-anchor: middle; }
  .rule { stroke: var(--text); stroke-width: 2; opacity: .7; }
  .m-basis .disc { fill: var(--basis); }
  .m-bde .disc { fill: var(--bde); }
  .m-alarm .disc { fill: var(--alarm); }
  .m-mde .disc { fill: var(--mde); }
  .m-inst .disc { fill: var(--inst); }
  .m-plan .disc { fill: var(--plan); }
  .m-tnt .disc { fill: var(--tnt); }
  .m-dok .disc { fill: var(--dok); }
  .m-pep .disc { fill: var(--pep); }
  .m-mpze .disc { fill: var(--mpze); }
  .m-log .disc { fill: var(--log); }
  .m-vis .disc { fill: var(--vis); }
  .m-dnc .disc { fill: var(--dnc); }
  .m-em .disc { fill: var(--em); }
</style>
</head>
<body>
<div class="canvas">
<svg class="module-map" width="1200" height="1050" viewBox="0 0 1200 1050" xmlns="http://www.w3.org/2000/svg">
  <defs>
    <filter id="ring-shadow" x="-20%" y="-20%" width="140%" height="140%">
      <feDropShadow dx="0" dy="2" stdDeviation="3" flood-color="#000" flood-opacity=".15"/>
    </filter>
    <g id="network">
      <line x1="605" y1="207" x2="405" y2="315"/><line x1="605" y1="207" x2="799" y2="315"/><line x1="605" y1="207" x2="605" y2="419"/>
      <line x1="405" y1="315" x2="207" y2="423"/><line x1="405" y1="315" x2="605" y2="419"/><line x1="405" y1="315" x2="405" y2="527"/>
      <line x1="799" y1="315" x2="605" y2="419"/><line x1="799" y1="315" x2="1001" y2="423"/><line x1="799" y1="315" x2="799" y2="527"/>
      <line x1="207" y1="423" x2="405" y2="527"/><line x1="207" y1="423" x2="207" y2="637"/>
      <line x1="605" y1="419" x2="405" y2="527"/><line x1="605" y1="419" x2="799" y2="527"/><line x1="605" y1="419" x2="605" y2="633"/>
      <line x1="1001" y1="423" x2="799" y2="527"/><line x1="1001" y1="423" x2="1001" y2="637"/>
      <line x1="405" y1="527" x2="207" y2="637"/><line x1="405" y1="527" x2="605" y2="633"/><line x1="405" y1="527" x2="405" y2="742"/>
      <line x1="799" y1="527" x2="605" y2="633"/><line x1="799" y1="527" x2="1001" y2="637"/><line x1="799" y1="527" x2="799" y2="742"/>
      <line x1="207" y1="637" x2="405" y2="742"/><line x1="605" y1="633" x2="405" y2="742"/><line x1="605" y1="633" x2="799" y2="742"/><line x1="605" y1="633" x2="605" y2="848"/>
      <line x1="1001" y1="637" x2="799" y2="742"/><line x1="405" y1="742" x2="605" y2="848"/><line x1="799" y1="742" x2="605" y2="848"/>
    </g>
  </defs>

  <use href="#network" class="link-edge"/>
  <use href="#network" class="link-core"/>

  <g class="module m-basis" transform="translate(605,207)">
    <circle class="ring" r="92" filter="url(#ring-shadow)"/><circle class="disc" r="82"/>
    <text class="code" y="-14">BASIS</text><text class="name" y="12">Basismodul</text>
    <line class="rule" x1="-18" y1="32" x2="18" y2="32"/>
  </g>
  <g class="module m-bde" transform="translate(405,315)">
    <circle class="ring" r="92" filter="url(#ring-shadow)"/><circle class="disc" r="82"/>
    <text class="code" y="-14">BDE</text><text class="name" y="12">Betriebsdatenerfassung</text>
    <line class="rule" x1="-18" y1="32" x2="18" y2="32"/>
  </g>
  <g class="module m-alarm" transform="translate(799,315)">
    <circle class="ring" r="92" filter="url(#ring-shadow)"/><circle class="disc" r="82"/>
    <text class="code" y="-14">ALARM</text><text class="name" y="12">Alarmierung</text>
    <line class="rule" x1="-18" y1="32" x2="18" y2="32"/>
  </g>
  <g class="module m-mde" transform="translate(207,423)">
    <circle class="ring" r="92" filter="url(#ring-shadow)"/><circle class="disc" r="82"/>
    <text class="code" y="-14">MDE</text><text class="name" y="12">Maschinendatenerfassung</text>
    <line class="rule" x1="-18" y1="32" x2="18" y2="32"/>
  </g>
  <g class="module m-inst" transform="translate(605,419)">
    <circle class="ring" r="92" filter="url(#ring-shadow)"/><circle class="disc" r="82"/>
    <text class="code" y="-14">INST</text><text class="name" y="12">Instandhaltung</text>
    <line class="rule" x1="-18" y1="32" x2="18" y2="32"/>
  </g>
  <g class="module m-plan" transform="translate(1001,423)">
    <circle class="ring" r="92" filter="url(#ring-shadow)"/><circle class="disc" r="82"/>
    <text class="code" y="-14">PLAN</text><text class="name" y="12">Feinplanung/Leitstand</text>
    <line class="rule" x1="-18" y1="32" x2="18" y2="32"/>
  </g>
  <g class="module m-tnt" transform="translate(405,527)">
    <circle class="ring" r="92" filter="url(#ring-shadow)"/><circle class="disc" r="82"/>
    <text class="code" y="-14">TNT</text><text class="name" y="12">Traceability</text>
    <line class="rule" x1="-18" y1="32" x2="18" y2="32"/>
  </g>
  <g class="module m-dok" transform="translate(799,527)">
    <circle class="ring" r="92" filter="url(#ring-shadow)"/><circle class="disc" r="82"/>
    <text class="code" y="-14">DOK</text><text class="name" y="12">Dokumentenmanagement</text>
    <line class="rule" x1="-18" y1="32" x2="18" y2="32"/>
  </g>
  <g class="module m-pep" transform="translate(207,637)">
    <circle class="ring" r="92" filter="url(#ring-shadow)"/><circle class="disc" r="82"/>
    <text class="code" y="-14">PEP</text><text class="name" y="12">Personaleinsatzplanung</text>
    <line class="rule" x1="-18" y1="32" x2="18" y2="32"/>
  </g>
  <g class="module m-mpze" transform="translate(605,633)">
    <circle class="ring" r="92" filter="url(#ring-shadow)"/><circle class="disc" r="82"/>
    <text class="code" y="-14">MPZE</text><text class="name" y="12">Personalzeiterfassung</text>
    <line class="rule" x1="-18" y1="32" x2="18" y2="32"/>
  </g>
  <g class="module m-log" transform="translate(1001,637)">
    <circle class="ring" r="92" filter="url(#ring-shadow)"/><circle class="disc" r="82"/>
    <text class="code" y="-14">LOG</text><text class="name" y="12">Logistik</text>
    <line class="rule" x1="-18" y1="32" x2="18" y2="32"/>
  </g>
  <g class="module m-vis" transform="translate(405,742)">
    <circle class="ring" r="92" filter="url(#ring-shadow)"/><circle class="disc" r="82"/>
    <text class="code" y="-14">VIS</text><text class="name" y="12">Visualisierung</text>
    <line class="rule" x1="-18" y1="32" x2="18" y2="32"/>
  </g>
  <g class="module m-dnc" transform="translate(799,742)">
    <circle class="ring" r="92" filter="url(#ring-shadow)"/><circle class="disc" r="82"/>
    <text class="code" y="-14">DNC</text><text class="name" y="12">Rezepturen/DNC</text>
    <line class="rule" x1="-18" y1="32" x2="18" y2="32"/>
  </g>
  <g class="module m-em" transform="translate(605,848)">
    <circle class="ring" r="92" filter="url(#ring-shadow)"/><circle class="disc" r="82"/>
    <text class="code" y="-14">EM</text><text class="name" y="12">Energiemonitoring</text>
    <line class="rule" x1="-18" y1="32" x2="18" y2="32"/>
  </g>
</svg>
</div>
</body>
</html>
```